Business card design for a content marketing agency

Need a business card design suitable for a digital marketing agency. Needs to be a bold and creative, high quality design that exudes expertise and professionalism, and instills in prospective new customers a sense of confidence that we are the right company to do business with. Specifications must meet PrintaNova requirement for extra thick matte stock. Needs to incorporate logo, tagline, name, title, website url, address, city, state, zip code, and mobile number.. I spec'd s single side design but I'm to a double sided design if it's strong and compelling. I like the use of icons associated with contact info, but it's not a requirement. Mostly, the design needs to command attention because it's so good or unusual. I have all kinds of files in large thru small sizes in jpg andpgn. pick from what you need, and let me know if you have questions.

Target Market(s)

CEO, Mktg VP's and small to medium size tech and prof'l service businesses

Industry/Entity Type

Marketing

Contact Information for Business Card

Owen Fairly
Chief Executive Officer
417 Larkfield Mill Lane
Alderby, MA 02938
owen@quellarmedia.example
www.quellarmedia.example
555-555-0162

Font styles to use
Sans Serif

Colors
0692cd
9bcb3c

Requirements
Must have
• Tagline is "Marketing That Audiences Value".
• Needs to be a bold and creative, high quality design that exudes expertise and professionalism, and instills in prospective new customers a sense of confidence that we are the right company to do business with. Specifications must meet PrintaNova requirement for extra thick matte stock. Needs to incorporate logo, tagline, name, title, website url, address, city, state, zip code, and mobile number..
Nice to have
• I spec'd s single side design but I'm open to a double sided design if it's strong and compelling. I like the use of icons associated with contact info, but it's not a requirement.
Should not have
• Chose colors that are the same and/or compatible with colors in the logo

```html
<!DOCTYPE html>
<html lang="en">
<head>
<meta charset="utf-8">
<title>Quellar Media – Business Card</title>
<link rel="stylesheet" href="https://fonts.googleapis.com/css2?family=Lato:wght@400;700&display=swap">
<style>
  :root {
    --bg: #2b2c2e;
    --brand-blue: #0692cd;
    --band-blue: #1f78c1;
    --band-blue-deep: #1765ad;
    --poly-light: #2a8ad8;
    --poly-dark: #0f5aa6;
    --paper: #f4f5f6;
    --ink: #1d2230;
    --navy: #13305a;
    --rule: #16181c;
    --white: #ffffff;
  }
  * { margin: 0; padding: 0; box-sizing: border-box; }
  html, body { width: 1200px; height: 997px; overflow: hidden; }
  body {
    background: var(--bg);
    font-family: "Lato", Arial, sans-serif;
    display: flex;
    flex-direction: column;
    align-items: center;
    justify-content: center;
    gap: 56px;
  }
  .card {
    position: relative;
    width: 620px;
    height: 354px;
    overflow: hidden;
    box-shadow: 0 14px 30px rgba(0,0,0,.45);
  }

  /* Back side */
  .card-back .pattern {
    position: absolute; inset: 0;
    background: linear-gradient(135deg, var(--poly-light) 0%, var(--brand-blue) 35%, var(--poly-dark) 70%, var(--poly-light) 100%);
  }
  .card-back .lockup {
    position: absolute;
    left: 50%; top: 50%;
    transform: translate(-50%, -50%);
    color: var(--white);
    white-space: nowrap;
  }
  .brand-row { display: flex; align-items: center; gap: 12px; }
  .brand-mark { width: 22px; height: 22px; flex: none; }
  .brand-name { font-size: 38px; font-weight: 700; line-height: 1.1; }
  .tagline { font-size: 15px; margin-left: 34px; margin-top: 3px; }
  .card-back .brand-mark { background: var(--white); }

  /* Front side */
  .card-front { background: linear-gradient(180deg, var(--white), var(--paper)); }
  .card-front .band { position: absolute; inset: 0; }
  .card-front .lockup { position: absolute; left: 170px; top: 64px; white-space: nowrap; }
  .card-front .brand-mark { background: var(--brand-blue); }
  .card-front .brand-name { color: var(--brand-blue); }
  .card-front .tagline { color: var(--ink); }

  .person { position: absolute; left: 38px; top: 242px; }
  .person .name { font-size: 22px; font-weight: 700; color: var(--white); letter-spacing: 1px; text-transform: uppercase; line-height: 26px; }
  .person .title { font-size: 15px; color: var(--navy); line-height: 20px; }

  .contact { position: absolute; left: 38px; top: 292px; list-style: none; font-size: 13px; color: var(--white); }
  .contact li { display: flex; align-items: center; gap: 9px; line-height: 18px; }
  .contact svg { width: 12px; height: 12px; fill: var(--ink); flex: none; }
  .contact .no-icon { padding-left: 21px; }

  .address {
    position: absolute; right: 30px; top: 180px;
    text-align: right; font-size: 13px; line-height: 19px; color: var(--navy);
  }
</style>
</head>
<body>

  <section class="card card-back" aria-label="Card back">
    <div class="pattern" role="img" aria-label="Blue low-poly faceted background pattern"></div>
    <div class="lockup">
      <div class="brand-row">
        <span class="brand-mark"></span>
        <span class="brand-name">Quellar Media</span>
      </div>
      <p class="tagline">Marketing That Audiences Value</p>
    </div>
  </section>

  <section class="card card-front" aria-label="Card front">
    <svg class="band" viewBox="0 0 620 354" preserveAspectRatio="none" aria-hidden="true">
      <defs>
        <linearGradient id="bandFill" x1="0" y1="0" x2="1" y2="1">
          <stop offset="0" stop-color="#1f78c1"/>
          <stop offset="1" stop-color="#1765ad"/>
        </linearGradient>
      </defs>
      <path d="M0,230 L40,224.8 L50,234 L60,222.3 L620,150 L620,354 L0,354 Z" fill="url(#bandFill)"/>
      <path d="M0,230 L40,224.8 L50,234 L60,222.3 L620,150" fill="none" stroke="#16181c" stroke-width="3"/>
    </svg>

    <div class="lockup">
      <div class="brand-row">
        <span class="brand-mark"></span>
        <span class="brand-name">Quellar Media</span>
      </div>
      <p class="tagline">Marketing That Audiences Value</p>
    </div>

    <div class="address">
      <p>Quellar Media</p>
      <p>417 Larkfield Mill Lane</p>
      <p>Alderby, MA 02938</p>
    </div>

    <div class="person">
      <p class="name">Owen Fairly</p>
      <p class="title">Chief Executive Officer</p>
    </div>

    <ul class="contact">
      <li>
        <svg viewBox="0 0 12 12" aria-hidden="true"><path d="M3 0h6a1 1 0 0 1 1 1v10a1 1 0 0 1-1 1H3a1 1 0 0 1-1-1V1a1 1 0 0 1 1-1zm0 1.5v8h6v-8z"/></svg>
        <span>555-555-0162</span>
      </li>
      <li>
        <svg viewBox="0 0 12 12" aria-hidden="true"><path d="M0 2h12v8H0zm1 1l5 3.5L11 3z"/></svg>
        <span>owen@quellarmedia.example</span>
      </li>
      <li class="no-icon"><span>www.quellarmedia.example</span></li>
    </ul>
  </section>

</body>
</html>
```